Medical Centre Website

We need a new design for a medical centre based in Perth, Western Australia called 'Tarvin Grove Medical Centre'.

The medical centre does general practitioner work including general checkups, ecg, heart checks, woman's health and more servicing children and adults. They also do home visits on occasions where the patient cannot attend the centre.

They would like an information/brochure website where visitors can read up on the practice, send email and view their location.

The client wish the design to be clean, fresh and light. The main colours are a light purple/blue and to a dark navy blue. The client would not want the logo to be altered in any way. This includes changing the words colours or the image.

The final design should represent a loving, family friendly practice where patients can come to receive the best treatments.

We just need the end product to be presented to un in a layed psd format. The fonts must be as per the W3C standards.

**IMPORTANT**
I have received heaps of chatlink invites in the past. To treat everyone fairly, I do not add people to my chatlink list as in the past people expected us to give them the prize. If you have questions, please ask them in pixel forum as it may benefit others who are also designing the site. If I need to, I will send a message to the user.
Updates

Hi Designers,

Most designs we have received have been overly cluttered. Are you able to simplify the designs.

Cheers, Dorian

Hi Designers,

Some of the designs are quite attractive but aremore cluttered than I would like. If you have a look at the following design, the design is very simple and straight to the point. A lot of designs have too much wording and the reader can be put off. We are looking something more like:

velmoxa.com.au

I would prefer to see designs and have opened up the contest for a further 7 days.

Designers,

We have received feedback from the client and Quite frankly he don’t really like any of them.They are too cluttered and Americanised. All drab blue colours.
 
If you have a look at template monster, these designs are better and cleaner. We do not want heaps of writing on the front page.

If you look at the eariler examples such as quorbeyclinic.com.au which I did myself, the client loves that simplicity of the site.

```html
<!DOCTYPE html>
<html lang="en">
<head>
<meta charset="utf-8">
<title>Tarvin Grove Medical Centre</title>
<link href="https://fonts.googleapis.com/css2?family=Arimo:ital,wght@0,400;0,700;1,400&family=Tinos:ital,wght@0,400;0,700;1,400&display=swap" rel="stylesheet">
<style>
:root{
  --navy:#1d3d7a;
  --blue:#2a78c8;
  --blue-dark:#1b5fa8;
  --blue-light:#4f9ae0;
  --sky:#eef3f9;
  --text:#444;
  --muted:#777;
  --line:#d9dee5;
  --white:#fff;
}
*{box-sizing:border-box;margin:0;padding:0}
html,body{width:888px;height:1200px;overflow:hidden;background:var(--white)}
body{font-family:"Arimo",Arial,sans-serif;color:var(--text);position:relative}
.site-header{position:absolute;left:26px;top:22px;right:26px;height:80px}
.brand{display:flex;align-items:center;gap:14px}
.brand-mark{width:30px;height:30px;border-radius:50%;background:var(--blue)}
.brand-name{font-family:"Tinos",serif;font-size:36px;color:var(--navy);line-height:1}
.phone{position:absolute;right:0;top:16px;display:flex;align-items:center;gap:8px;font-family:"Arimo",sans-serif;font-style:italic;font-size:24px;color:#888}
.main-nav{position:absolute;left:26px;top:116px;width:836px;height:44px;background:linear-gradient(#3d8ad6,var(--blue-dark));border-radius:6px 6px 0 0;display:flex;padding-left:10px}
.main-nav a{color:var(--white);text-decoration:none;font-weight:700;font-size:15px;line-height:44px;padding:0 28px;border-right:1px solid rgba(255,255,255,.25)}
.main-nav a.active{background:rgba(255,255,255,.12);border-bottom:3px solid var(--white)}
.hero{position:absolute;left:26px;top:160px;width:836px;height:303px;background:linear-gradient(#f7f9fc,var(--sky));border:1px solid var(--line);overflow:hidden}
.hero-title{position:absolute;left:72px;top:46px;font-family:"Tinos",serif;font-style:italic;font-size:70px;color:var(--blue);font-weight:400}
.hero-quote{position:absolute;left:60px;top:140px;width:440px;text-align:center;font-family:"Tinos",serif;font-style:italic;font-size:28px;line-height:1.35;color:var(--blue)}
.hero-photo{position:absolute;right:40px;top:0;width:240px;height:303px;background:linear-gradient(#e6ecf3,#c9b8ae 55%,#8da3c2)}
.hero-dots{position:absolute;right:18px;bottom:14px;display:flex;gap:6px}
.hero-dots span{width:10px;height:10px;border-radius:50%;background:#c5ccd6}
.hero-dots span.on{background:var(--blue)}
.services{position:absolute;left:26px;top:482px;width:836px;display:flex;justify-content:space-between}
.service{width:192px}
.service-photo{height:112px;border:1px solid var(--line);border-bottom:none}
.service-label{height:44px;background:linear-gradient(var(--blue-light),var(--blue-dark));border-radius:0 0 6px 6px;color:var(--white);font-family:"Tinos",serif;font-style:italic;font-size:24px;text-align:center;line-height:44px;letter-spacing:1px}
.content{position:absolute;left:26px;top:660px;width:622px}
.post{padding-bottom:22px;margin-bottom:24px;border-bottom:1px dotted var(--line)}
.post-title{font-family:"Tinos",serif;font-style:italic;font-size:28px;color:var(--blue);font-weight:400}
.post-sub{font-weight:700;font-size:13.5px;color:#222;margin:6px 0 6px}
.post p{font-size:10.5px;line-height:1.45;color:var(--muted);margin-bottom:8px}
.more{color:var(--blue);font-weight:700;font-style:italic;text-decoration:none}
.sidebar{position:absolute;left:668px;top:655px;width:194px}
.categories{border:1px solid var(--line);background:#fafbfc}
.categories h3{font-family:"Tinos",serif;font-style:italic;font-size:21px;color:#333;font-weight:400;padding:8px 16px;background:linear-gradient(#fff,#eceff3);border-bottom:1px solid var(--line)}
.categories ul{list-style:none;padding:12px 16px 10px}
.categories li{font-family:"Tinos",serif;font-style:italic;font-size:20px;color:var(--blue);line-height:33px;display:flex;align-items:center;gap:10px}
.social{display:flex;gap:10px;justify-content:center;margin-top:26px}
.social span{width:56px;height:56px;border-radius:8px;font-family:"Arimo",sans-serif;font-size:9px;color:var(--white);display:flex;align-items:flex-end;justify-content:center;padding-bottom:6px}
.social .circlebook{background:#3b5a9a}
.social .chirpline{background:#45b0e3}
</style>
</head>
<body>
<header class="site-header">
  <div class="brand">
    <span class="brand-mark"></span>
    <span class="brand-name">Tarvin Grove Medical Centre</span>
  </div>
  <div class="phone">
    <svg width="20" height="20" viewBox="0 0 24 24"><path fill="#2a78c8" d="M6.6 10.8a15 15 0 0 0 6.6 6.6l2.2-2.2c.3-.3.7-.4 1-.2 1.1.4 2.3.6 3.6.6.6 0 1 .4 1 1V20c0 .6-.4 1-1 1A17 17 0 0 1 3 4c0-.6.4-1 1-1h3.5c.6 0 1 .4 1 1 0 1.3.2 2.5.6 3.6.1.3 0 .7-.2 1z"/></svg>
    (08) 9555 0142
  </div>
</header>

<nav class="main-nav">
  <a class="active" href="#">Home</a>
  <a href="#">Services</a>
  <a href="#">Blog</a>
  <a href="#">Contacts</a>
</nav>

<section class="hero">
  <h1 class="hero-title">Lorem Ipsum</h1>
  <p class="hero-quote">"Neque porro quisquam est qui dolorem ipsum quia dolor sit amet,.."</p>
  <div class="hero-photo" role="img" aria-label="Smiling family of mother, father and young daughter"></div>
  <div class="hero-dots"><span class="on"></span><span></span><span></span></div>
</section>

<section class="services">
  <div class="service"><div class="service-photo" role="img" aria-label="Woman resting on a pillow" style="background:linear-gradient(#f4ede6,#d9c3b0)"></div><div class="service-label">Service 1</div></div>
  <div class="service"><div class="service-photo" role="img" aria-label="Hands breaking a cigarette" style="background:linear-gradient(#cfe1ef,#e8d9c9)"></div><div class="service-label">Service 2</div></div>
  <div class="service"><div class="service-photo" role="img" aria-label="Woman with a headache" style="background:linear-gradient(#eceae6,#c8b8a8)"></div><div class="service-label">Service 3</div></div>
  <div class="service"><div class="service-photo" role="img" aria-label="Smiling family group outdoors" style="background:linear-gradient(#a9bf8e,#d8b79c)"></div><div class="service-label">Service 4</div></div>
</section>

<main class="content">
  <article class="post">
    <h2 class="post-title">LoremIpsum1</h2>
    <p class="post-sub">Lorem ipsum dolor sit amet conse ctetur adipisicing eli</p>
    <p>Lorem ipsum dolor sit amet, consectetur adipisicing elit, sed do eiusmod tempor incididunt ut labore et dolore magna aliqua. Ut enim ad minim veniam, quis nostrud exercitation ullamco laboris nisi ut aliquip ex ea commodo consequat. Duis aute irure dolor in reprehenderit in voluptate velit esse cillum dolore eu fugiat nulla pariatur. Excepteur sint occaecat cupidatat non proident, sunt in culpa qui officia deserunt mollit anim id est laborum. <a class="more" href="#">Read more »</a></p>
  </article>
  <article class="post">
    <h2 class="post-title">LoremIpsum2</h2>
    <p class="post-sub">Dolor sit amet conse ctetur adipisicing eli</p>
    <p>Lorem ipsum dolor sit amet, consectetur adipisicing elit, sed do eiusmod tempor incididunt ut labore et dolore magna aliqua. Ut enim ad minim veniam, quis nostrud exercitation ullamco laboris nisi ut aliquip ex ea commodo consequat. Duis aute irure dolor in reprehenderit in voluptate velit esse cillum dolore eu fugiat nulla pariatur. Excepteur sint occaecat cupidatat non proident, sunt in culpa qui officia deserunt mollit anim id est laborum.</p>
    <p>Ctetur adipisicing elit, sed do eiusmod tempor incididunt ut labore et dolore magna aliqua. Ut enim ad minim veniam, quis nostrud exercitation ullamco laboris nisi ut aliquip ex ea commodo consequat. Duis aute irure dolor in reprehenderit in voluptate velit esse cillum dolore eu fugiat nulla pariatur. <a class="more" href="#">Read more »</a></p>
  </article>
  <article class="post">
    <h2 class="post-title">LoremIpsum1</h2>
    <p class="post-sub">Excepteur sint occaecat cupidatat non proident, sunt in culpa qui o</p>
    <p>Lorem ipsum dolor sit amet, consectetur adipisicing elit, sed do eiusmod tempor incididunt ut labore et dolore magna aliqua. Ut enim ad minim veniam, quis nostrud exercitation ullamco laboris nisi ut aliquip ex ea commodo consequat. Duis aute irure dolor in reprehenderit in voluptate velit esse cillum dolore eu fugiat nulla pariatur. Excepteur sint occaecat cupidatat non proident, sunt in culpa qui officia deserunt mollit anim id est laborum. <a class="more" href="#">Read more »</a></p>
  </article>
</main>

<aside class="sidebar">
  <section class="categories">
    <h3>Categories</h3>
    <ul>
      <li><svg width="10" height="10" viewBox="0 0 10 10"><path d="M1 1l4 4-4 4M5 1l4 4-4 4" fill="none" stroke="#2a78c8" stroke-width="1.3"/></svg>LoremIpsum 1</li>
      <li><svg width="10" height="10" viewBox="0 0 10 10"><path d="M1 1l4 4-4 4M5 1l4 4-4 4" fill="none" stroke="#2a78c8" stroke-width="1.3"/></svg>LoremIpsum 2</li>
      <li><svg width="10" height="10" viewBox="0 0 10 10"><path d="M1 1l4 4-4 4M5 1l4 4-4 4" fill="none" stroke="#2a78c8" stroke-width="1.3"/></svg>LoremIpsum 3</li>
      <li><svg width="10" height="10" viewBox="0 0 10 10"><path d="M1 1l4 4-4 4M5 1l4 4-4 4" fill="none" stroke="#2a78c8" stroke-width="1.3"/></svg>LoremIpsum 4</li>
      <li><svg width="10" height="10" viewBox="0 0 10 10"><path d="M1 1l4 4-4 4M5 1l4 4-4 4" fill="none" stroke="#2a78c8" stroke-width="1.3"/></svg>LoremIpsum 5</li>
    </ul>
  </section>
  <div class="social">
    <span class="circlebook">Circlebook</span>
    <span class="chirpline">Chirpline</span>
  </div>
</aside>
</body>
</html>
```